Allied Health team of Physiotherapists & Occupational Therapists seek a business card design

We have our new logo, we now need our new business cards and stationary. Blossom: Lymphoedema & Women's Clinic is seeking a generic card design to represent our whole team and individual cards for each therapist that incorporates our new logo to communicate our holistic approach that is calming, nuturing, supportive and welcoming.
Our Physiotherapists and Occupational Therapists assess, treat and provide education for people who are at risk of or who have lymphoedema. This is often as a result of treatment for cancer. We provide pre-operative and post-operative management and cancer rehabilitation in our Pilates studio. Our team also consists of Physiotherapists who have a strong interest in pelvic floor and continence management for both men and women.

Target Market(s)

Mainly women health conscious

Industry/Entity Type

Allied Health: Physiotherapy / Occupational Therapy

Contact Information for Business Card

Address: 14 Calloway Ave Frankston 3199 Phone: 84317560 fax: 8431 7564 Email: info@blossomcarepartners.com.au Website: blossomcarepartners.com.au Facebook address: facebook.com/BlossomLymphoedemaAndWomensCareCentre. Room to write appointments. Individual cards need to have name, office email and individual email and professional details

Requirements
Must have
• Logo as per uploaded documents

```html
<!DOCTYPE html>
<html lang="en">
<head>
<meta charset="utf-8">
<title>Blossom Business Card</title>
<link rel="stylesheet" href="https://fonts.googleapis.com/css2?family=Carlito:wght@400;700&family=Tenor+Sans&display=swap">
<style>
  :root {
    --backdrop: #2b2b2c;
    --card: #1d1d1f;
    --card-edge: #151516;
    --cream: #f1ebcf;
    --ink-light: #f4f4f2;
    --rule: #6a6a6a;
    --pattern-a: #222224;
    --pattern-b: #1a1a1c;
  }
  * { margin: 0; padding: 0; box-sizing: border-box; }
  html, body {
    width: 1200px; height: 1108px; overflow: hidden;
    background: var(--backdrop);
  }
  .stage {
    position: relative; width: 1200px; height: 1108px;
    display: flex; justify-content: center; align-items: center; gap: 70px;
  }
  .card {
    position: relative; width: 440px; height: 680px;
    background: var(--card); border-radius: 26px;
    box-shadow: 0 14px 30px rgba(0,0,0,.45);
    overflow: hidden;
  }
  .card-front {
    display: flex; flex-direction: column; align-items: center;
    padding-top: 92px; text-align: center;
    font-family: "Carlito", "Calibri", sans-serif; color: var(--ink-light);
  }
  .therapist-name {
    font-family: "Tenor Sans", sans-serif; font-weight: 400;
    font-size: 30px; letter-spacing: 3px; color: var(--cream);
    margin-bottom: 10px;
  }
  .credentials { font-size: 21px; line-height: 1.3; }
  .roles {
    margin-top: 16px; font-size: 21px; font-weight: 700; line-height: 1.3;
  }
  .divider {
    width: 70px; height: 1px; background: var(--rule);
    margin: 34px 0 30px;
  }
  .contacts { font-size: 21px; line-height: 1.36; }
  .card-back { display: flex; justify-content: center; align-items: center; }
  .backdrop-pattern {
    position: absolute; inset: 0;
    background: linear-gradient(160deg, var(--pattern-a), var(--pattern-b));
  }
  .brand {
    position: relative; display: flex; flex-direction: column; align-items: center; gap: 14px;
  }
  .brand-dot {
    width: 22px; height: 22px; border-radius: 50%;
    border: 2px solid var(--cream);
  }
  .brand-name {
    font-family: "Carlito", "Calibri", sans-serif; font-size: 52px;
    font-weight: 400; color: var(--cream); letter-spacing: 1px;
  }
</style>
</head>
<body>
  <main class="stage">
    <section class="card card-front">
      <h1 class="therapist-name">MAREN ASHBY</h1>
      <p class="credentials">
        B. Physio (Hons), B.App.Sci.<br>
        (Human Movement/Psych)<br>
        Post Grad Certif. Exercise for Women<br>
        Post Grad Certif. Continence &amp;<br>
        Pelvic Floor Rehabilitation
      </p>
      <p class="roles">
        Physiotherapist<br>
        Lymphoedema &amp; Oncology Rehabilitation<br>
        Continence &amp; Pelvic Floor
      </p>
      <div class="divider"></div>
      <p class="contacts">
        000 1111 2222<br>
        info@blossomcarepartners.com.au<br>
        name@blossomcarepartners.com.au<br>
        www.blossomcarepartners.com.au
      </p>
    </section>
    <section class="card card-back">
      <div class="backdrop-pattern" role="img" aria-label="Faint repeating brand-name pattern across the card back"></div>
      <div class="brand">
        <span class="brand-dot"></span>
        <span class="brand-name">Blossom</span>
      </div>
    </section>
  </main>
</body>
</html>
```